Lena Corvell Business Card

I need a business card that reflects my current website: itslenacorvell.example and screenshot attached. If we keep the color scheme of the site and sample card below that would be ideal. The business card should include the information on the attached sample cards.

Industry/Entity Type

Business

```html
<!DOCTYPE html>
<html lang="en">
<head>
<meta charset="utf-8">
<title>Lena Corvell Business Card Options</title>
<link rel="stylesheet" href="https://fonts.googleapis.com/css2?family=Didact+Gothic&family=Open+Sans:wght@400;700&display=swap">
<style>
  :root {
    --page: #ebebeb;
    --teal: #5fbfad;
    --teal-deep: #2ea897;
    --ink: #333333;
    --ink-soft: #4a4a4a;
    --white: #ffffff;
    --black: #1e1e1e;
    --photo-light: #8a8482;
    --photo-dark: #5d5856;
    --label: #3c3c3c;
  }
  * { box-sizing: border-box; margin: 0; padding: 0; }
  html, body { width: 699px; height: 1200px; overflow: hidden; }
  body {
    background: var(--page);
    position: relative;
    font-family: "Didact Gothic", "Century Gothic", sans-serif;
  }
  .option-number {
    position: absolute;
    left: 33px;
    font-family: "Open Sans", Arial, sans-serif;
    font-size: 24px;
    color: var(--label);
  }
  .card {
    position: absolute;
    overflow: hidden;
    box-shadow: 2px 3px 6px rgba(0,0,0,0.18);
  }
  .card-art { position: absolute; left: 0; top: 0; }
  .card-text { position: absolute; }
  .name {
    font-family: "Open Sans", Arial, sans-serif;
    font-weight: 700;
    font-size: 16px;
    letter-spacing: 0.2px;
  }
  .title {
    font-family: "Open Sans", Arial, sans-serif;
    font-size: 11.5px;
    margin-top: 5px;
    white-space: nowrap;
  }
  .contacts { list-style: none; }
  .contacts li {
    display: flex;
    align-items: center;
    font-size: 19px;
    white-space: nowrap;
    height: 20px;
  }
  .icon { width: 16px; height: 16px; margin-right: 8px; flex: none; }
  .social-mark { width: 14px; height: 14px; border: 1.5px solid currentColor; margin-right: 8px; flex: none; }

  /* Option 1 */
  .card-teal { left: 80px; top: 58px; width: 533px; height: 298px; background: var(--teal); }
  .card-teal .card-text { left: 28px; top: 35px; color: var(--white); }
  .card-teal .contacts { margin-top: 32px; }
  .card-teal .contacts li + li { margin-top: 15px; }

  /* Option 2 */
  .card-white { left: 77px; top: 418px; width: 534px; height: 297px; background: var(--white); }
  .card-white .card-text { left: 25px; top: 35px; color: var(--ink); }
  .card-white .title { color: var(--teal-deep); font-weight: 700; font-size: 11.5px; }
  .card-white .contacts { margin-top: 42px; color: var(--ink-soft); }
  .card-white .contacts li + li { margin-top: 15px; }
  .card-white .icon, .card-white .social-mark { color: var(--teal-deep); }

  /* Option 3 */
  .card-banded { left: 82px; top: 798px; width: 543px; height: 314px; background: var(--white); }
  .card-banded .card-text { left: 224px; top: 76px; color: var(--ink); }
  .card-banded .title { font-size: 11.5px; color: var(--ink-soft); }
  .card-banded .dot { color: var(--teal); }
  .card-banded .contacts { margin-top: 38px; color: var(--ink-soft); }
  .card-banded .contacts li + li { margin-top: 15px; }
  .card-banded .icon, .card-banded .social-mark { color: var(--teal-deep); }
</style>
</head>
<body>
<svg width="0" height="0" style="position:absolute" aria-hidden="true">
  <defs>
    <linearGradient id="portrait-tone" x1="0" y1="0" x2="1" y2="1">
      <stop offset="0" stop-color="#8d8886"/>
      <stop offset="0.55" stop-color="#6f6a68"/>
      <stop offset="1" stop-color="#57524f"/>
    </linearGradient>
    <symbol id="icon-mail" viewBox="0 0 16 16">
      <rect x="1.5" y="3.5" width="13" height="9" fill="none" stroke="currentColor" stroke-width="1.3"/>
      <path d="M1.5 3.5 L8 9 L14.5 3.5" fill="none" stroke="currentColor" stroke-width="1.3"/>
    </symbol>
    <symbol id="icon-phone" viewBox="0 0 16 16">
      <rect x="3.5" y="1.5" width="9" height="13" rx="1.5" fill="none" stroke="currentColor" stroke-width="1.3"/>
      <line x1="6.5" y1="12" x2="9.5" y2="12" stroke="currentColor" stroke-width="1.3"/>
    </symbol>
    <symbol id="icon-web" viewBox="0 0 16 16">
      <circle cx="8" cy="8" r="6.5" fill="none" stroke="currentColor" stroke-width="1.2"/>
      <ellipse cx="8" cy="8" rx="3" ry="6.5" fill="none" stroke="currentColor" stroke-width="1.1"/>
      <line x1="1.5" y1="8" x2="14.5" y2="8" stroke="currentColor" stroke-width="1.1"/>
      <line x1="2.5" y1="5" x2="13.5" y2="5" stroke="currentColor" stroke-width="1"/>
      <line x1="2.5" y1="11" x2="13.5" y2="11" stroke="currentColor" stroke-width="1"/>
    </symbol>
  </defs>
</svg>

<span class="option-number" style="top:198px">1</span>
<span class="option-number" style="top:580px">2</span>
<span class="option-number" style="top:962px">3</span>

<!-- Option 1: teal card -->
<section class="card card-teal">
  <svg class="card-art" width="533" height="298" viewBox="0 0 533 298">
    <polygon points="345,0 352,0 318,298 311,298" fill="var(--white)"/>
    <polygon points="352,0 358,0 324,298 318,298" fill="var(--black)"/>
    <g role="img" aria-label="Portrait photograph of Lena Corvell with signature lettering">
      <polygon points="358,0 533,0 533,298 324,298" fill="url(#portrait-tone)"/>
    </g>
  </svg>
  <div class="card-text">
    <p class="name">LENA CORVELL</p>
    <p class="title">Brand Curator I Digital Storyteller I Social Entrepreneur</p>
    <ul class="contacts">
      <li><svg class="icon"><use href="#icon-mail"/></svg>me@lenacorvell.example</li>
      <li><svg class="icon"><use href="#icon-phone"/></svg>555.013.2047</li>
      <li><svg class="icon"><use href="#icon-web"/></svg>www.itslenacorvell.example</li>
      <li><span class="social-mark"></span>@itslenacorvell</li>
    </ul>
  </div>
</section>

<!-- Option 2: white card -->
<section class="card card-white">
  <svg class="card-art" width="534" height="297" viewBox="0 0 534 297">
    <rect x="0" y="0" width="10" height="297" fill="var(--teal-deep)"/>
    <polygon points="352,14 366,14 325,297 311,297" fill="var(--teal-deep)"/>
    <g role="img" aria-label="Portrait photograph of Lena Corvell with signature lettering">
      <polygon points="366,0 534,0 534,297 325,297" fill="url(#portrait-tone)"/>
    </g>
  </svg>
  <div class="card-text">
    <p class="name">LENA CORVELL</p>
    <p class="title">Brand Curator I Digital Storyteller I Social Entrepreneur</p>
    <ul class="contacts">
      <li><svg class="icon"><use href="#icon-mail"/></svg>me@lenacorvell.example</li>
      <li><svg class="icon"><use href="#icon-phone"/></svg>555.013.2047</li>
      <li><svg class="icon"><use href="#icon-web"/></svg>www.itslenacorvell.example</li>
      <li><span class="social-mark"></span>@itslenacorvell</li>
    </ul>
  </div>
</section>

<!-- Option 3: banded card -->
<section class="card card-banded">
  <svg class="card-art" width="543" height="314" viewBox="0 0 543 314">
    <rect x="0" y="0" width="543" height="32" fill="var(--teal)"/>
    <rect x="0" y="304" width="543" height="10" fill="var(--teal)"/>
    <g role="img" aria-label="Portrait photograph of Lena Corvell with signature lettering">
      <rect x="0" y="32" width="213" height="272" fill="url(#portrait-tone)"/>
    </g>
  </svg>
  <div class="card-text">
    <p class="name">LENA CORVELL</p>
    <p class="title">Brand Curator<span class="dot">•</span>Digital Storyteller<span class="dot">•</span>Social Entrepreneur</p>
    <ul class="contacts">
      <li><svg class="icon"><use href="#icon-mail"/></svg>me@lenacorvell.example</li>
      <li><svg class="icon"><use href="#icon-phone"/></svg>555.013.2047</li>
      <li><svg class="icon"><use href="#icon-web"/></svg>www.itslenacorvell.example</li>
      <li><span class="social-mark"></span>@itslenacorvell</li>
    </ul>
  </div>
</section>
</body>
</html>
```